A layout of a webpage for oil trade platform

I would like to have a desgin of one page webpage (with section scrollling dowin) that woulf present the new product i.e. oil trade platform for wholesale buyers and sellers.
Layout should consist of the sections similar to the given at: https://klinika.pewnywybor.pl/system-zarzadzania-wizytami
However oil industy require more colors and more photo stories than here for doctor.
I. I woul imagine at first below menu a slider with brueg information about the product and its advantages with "more" button next to the prict screen of our platform on different displays (PC and mobile).
II. Bellow the slider I would imagine icons correspoing to the advantages of that plaftorm:
1. Purchase/sale process automation 24/7
2. Access to the best deals
3. Electronic offerings and orderings
4. Transaction status monitoring
5. Data and transaction security
II A) (optional):
In near future we would like to prepare a short video presenation. Hence please prepare a place to display that element here.
At the moment alternatvily please prepare a How it works section that would explan the platform operating process
III. Next secion is about benefits for Oil Purchaser
It can be done either by icons of by text and corresponding grahip for while section.
Benefits:
- Access to cheaper oil
- Convenience of online orders
- Possibility to compare prices on the market
- Transaction history
- Order status monitoring
- Seccurity and transparency of purchase
IV. Next seciont is about benefits for Oil Seller
Benefits:
- New sale channel
- Attracting new clients
- More oil sold
- Transaction security
- Possibility to integrate with distribution infrastructure and logistits for more efficient automation.
V. Contact form
VI. Footer
I would need a layout that that will correspond to the very dynamic logo but I would expect also a clean form, smoth and modern. It has to be proffessional layout with more corporate character.
It can use a paralax features if needed.

```html
<!DOCTYPE html>
<html lang="en">
<head>
<meta charset="utf-8">
<title>Crudeline – Oil Trade Platform</title>
<link rel="stylesheet" href="https://fonts.googleapis.com/css2?family=Open+Sans:wght@300;400;600&family=Oswald:wght@300;400&display=swap">
<style>
:root{
  --orange:#f5821f;
  --navy:#1f3252;
  --ink:#2b2b2b;
  --text:#555;
  --soft:#f6f6f6;
  --grey-band:#ebebeb;
  --line:#d9d9d9;
  --footer:#121212;
  --footer-bottom:#0a0a0a;
  --white:#fff;
}
*{box-sizing:border-box;margin:0;padding:0}
html,body{width:1200px;height:2927px;overflow:hidden}
body{font-family:'Open Sans',Arial,sans-serif;color:var(--text);background:var(--white);position:relative}
section,header,footer{position:absolute;left:0;width:1200px}
.abs{position:absolute}

/* header */
.site-header{top:0;height:101px;background:var(--white)}
.brand{position:absolute;display:flex;align-items:center;gap:10px;font-family:'Open Sans',sans-serif;font-weight:600}
.brand-dot{border-radius:50%;background:var(--orange)}
.site-header .brand{left:88px;top:28px;font-size:26px;color:var(--ink)}
.site-header .brand-dot{width:40px;height:40px}
.main-nav a{position:absolute;top:44px;font-size:15px;color:#444;text-decoration:none;letter-spacing:.3px;white-space:nowrap}
.main-nav a.active{color:var(--orange)}

/* hero */
.hero{top:101px;height:529px;background:linear-gradient(180deg,#233858 0%,#1b2c49 100%)}
.hero-title{left:86px;top:170px;font-family:'Oswald',sans-serif;font-weight:400;font-size:66px;color:var(--white);letter-spacing:1px;line-height:1}
.hero-sub{left:86px;top:252px;font-size:30px;color:var(--white);font-weight:400;white-space:nowrap}
.btn-more{left:86px;top:315px;width:97px;height:37px;border-radius:19px;background:var(--orange);color:var(--white);font-size:14px;display:flex;align-items:center;justify-content:center}
.slider-dot{top:385px;width:26px;height:26px;border-radius:50%;background:#111;display:flex;align-items:center;justify-content:center}
.devices{left:507px;top:84px;width:621px;height:361px;border-radius:6px;background:linear-gradient(135deg,#3a4a62 0%,#d9dee6 55%,#2a2f38 100%);opacity:.85}

/* features band */
.features{top:630px;height:205px;background:var(--soft);border-bottom:2px solid #e6e6e6}
.feature{position:absolute;top:38px;width:200px;margin-left:-100px;text-align:center}
.feature svg{display:block;margin:0 auto 20px}
.feature p{font-size:12.5px;line-height:21px;color:#333;text-transform:uppercase}

/* about */
.about{top:835px;height:443px;background:var(--white)}
.h-section{font-weight:400;color:var(--ink);text-transform:uppercase;line-height:1.2}
.about h2{position:absolute;left:92px;top:94px;font-size:24px}
.about .copy{left:92px;top:138px;width:478px;font-size:12.5px;line-height:20.5px;text-align:justify;color:#666}
.btn-outline{left:92px;top:324px;width:105px;height:33px;border:1.5px solid var(--orange);border-radius:17px;color:var(--orange);font-size:12px;display:flex;align-items:center;justify-content:center}
.video-frame{left:601px;top:74px;width:505px;height:293px;border:4px solid var(--white);box-shadow:0 0 0 1px var(--line);background:linear-gradient(135deg,#0b1526 0%,#1d3a66 50%,#0e1a2e 100%)}
.play{left:219px;top:113px;width:60px;height:60px;border-radius:50%;background:rgba(255,255,255,.85);display:flex;align-items:center;justify-content:center}

/* purchaser */
.purchaser{top:1278px;height:501px;background:linear-gradient(135deg,#f8f8f8,#f1f1f1)}
.purchaser h2,.seller h2{position:absolute;width:100%;text-align:center;font-size:28px}
.purchaser h2{top:70px}
.purchaser .lead{top:112px;width:100%;text-align:center;font-size:16px;color:#777}
.benefit{position:absolute;width:340px}
.benefit .ring{position:absolute;left:0;top:0;width:78px;height:78px;border-radius:50%;border:2px solid var(--line);background:var(--white);display:flex;align-items:center;justify-content:center}
.benefit h3{position:absolute;left:92px;top:16px;font-size:15px;font-weight:400;color:#222;text-transform:uppercase;white-space:nowrap}
.benefit p{position:absolute;left:92px;top:44px;width:245px;font-size:12.5px;line-height:20px;color:#888}
.rig{left:455px;top:181px;width:269px;height:229px;border-radius:8px;background:linear-gradient(180deg,#f3c64a 0%,#f5a24b 45%,#6fb6e0 100%);opacity:.8}

/* seller */
.seller{top:1779px;height:439px;background:var(--grey-band)}
.seller h2{top:66px}
.perk{position:absolute;top:141px;width:260px;margin-left:-130px;text-align:center}
.perk .ring{width:108px;height:108px;margin:0 auto;border-radius:50%;border:2px solid #bcbcbc;background:var(--white);display:flex;align-items:center;justify-content:center}
.perk h3{margin-top:26px;font-size:15px;font-weight:400;color:#222;text-transform:uppercase;white-space:nowrap}
.perk p{margin:18px auto 0;width:230px;font-size:12.5px;line-height:21px;color:#777}

/* contact */
.contact{top:2218px;height:420px;background:var(--white)}
.contact h2{position:absolute;font-size:24px}
.contact .copy{left:92px;top:143px;width:474px;font-size:12.5px;line-height:21.5px;text-align:justify;color:#666}
.field{position:absolute;height:52px;border:1.5px solid var(--line);border-radius:4px;background:var(--white);box-shadow:0 1px 3px rgba(0,0,0,.06);font-size:13px;color:#333;padding:16px 14px}
.btn-submit{left:1011px;top:316px;width:99px;height:36px;border-radius:18px;background:var(--orange);color:var(--white);font-size:14px;display:flex;align-items:center;justify-content:center}

/* footer */
.site-footer{top:2638px;height:207px;background:var(--footer);color:#ddd}
.site-footer .brand{left:98px;top:92px;font-size:26px;color:var(--white)}
.site-footer .brand-dot{width:40px;height:40px}
.site-footer h4{position:absolute;top:38px;font-size:13.5px;font-weight:400;color:var(--white);text-transform:uppercase;letter-spacing:.3px;white-space:nowrap}
.footer-lines{left:355px;top:76px;font-size:11.5px;line-height:20.5px;color:#ddd;white-space:nowrap}
.footer-note{left:646px;top:76px;width:190px;font-size:11.5px;line-height:19px;color:#ddd}
.news-input{left:646px;top:117px;width:146px;height:29px;background:var(--white);font-size:11px;color:#555;padding:7px 8px}
.news-btn{left:792px;top:117px;width:57px;height:29px;background:var(--orange);color:var(--white);font-size:11px;display:flex;align-items:center;justify-content:center}
.social{position:absolute;top:84px;width:26px;height:26px;border-radius:4px;background:var(--white)}
.copyright{top:2845px;height:82px;background:var(--footer-bottom);display:flex;align-items:center;justify-content:center;font-size:13px;color:#eee}
</style>
</head>
<body>

<header class="site-header">
  <div class="brand"><span class="brand-dot"></span>Crudeline</div>
  <nav class="main-nav">
    <a class="active" style="left:425px">HOME</a>
    <a style="left:509px">ABOUT US</a>
    <a style="left:626px">SERVICES</a>
    <a style="left:732px">OIL PURCHASER</a>
    <a style="left:890px">OIL SELLER</a>
    <a style="left:1013px">CONTACT US</a>
  </nav>
</header>

<section class="hero">
  <h1 class="abs hero-title">CRUDELINE</h1>
  <p class="abs hero-sub">Neque porro quisquam</p>
  <div class="abs btn-more">MORE &raquo;</div>
  <div class="abs slider-dot" style="left:90px"><svg width="10" height="10" viewBox="0 0 10 10"><path d="M7 1 3 5l4 4" fill="none" stroke="#fff" stroke-width="2"/></svg></div>
  <div class="abs slider-dot" style="left:122px"><svg width="10" height="10" viewBox="0 0 10 10"><path d="M3 1l4 4-4 4" fill="none" stroke="#fff" stroke-width="2"/></svg></div>
  <div class="abs devices" role="img" aria-label="Platform screens shown on a desktop monitor, laptop, tablet and phone"></div>
</section>

<section class="features">
  <div class="feature" style="left:195px">
    <svg width="34" height="34" viewBox="0 0 34 34"><circle cx="17" cy="17" r="14" fill="none" stroke="#999" stroke-width="3"/><path d="M17 9v9h6" fill="none" stroke="#999" stroke-width="3"/></svg>
    <p>Purchase/sale<br>process automation 24/7</p>
  </div>
  <div class="feature" style="left:392px">
    <svg width="34" height="34" viewBox="0 0 34 34"><circle cx="17" cy="10" r="7" fill="#999"/><path d="M4 33c0-9 6-14 13-14s13 5 13 14z" fill="#999"/></svg>
    <p>Access to the<br>best deals</p>
  </div>
  <div class="feature" style="left:583px">
    <svg width="34" height="34" viewBox="0 0 34 34"><path d="M14 8l12 12-6 6-12-12z" fill="#999"/><path d="M17 11l6-6M23 17l6-6M11 23l-8 8" stroke="#999" stroke-width="3"/></svg>
    <p>Electronic offerings<br>and orderings</p>
  </div>
  <div class="feature" style="left:775px">
    <svg width="38" height="34" viewBox="0 0 38 34"><rect x="2" y="3" width="34" height="22" rx="2" fill="none" stroke="#999" stroke-width="3"/><path d="M13 32h12M19 25v7" stroke="#999" stroke-width="3"/></svg>
    <p>Transaction status<br>monitoring</p>
  </div>
  <div class="feature" style="left:979px">
    <svg width="34" height="34" viewBox="0 0 34 34" fill="#999"><ellipse cx="17" cy="6" rx="13" ry="5"/><path d="M4 9c0 3 6 5 13 5s13-2 13-5v6c0 3-6 5-13 5S4 18 4 15zM4 18c0 3 6 5 13 5s13-2 13-5v6c0 3-6 5-13 5S4 27 4 24z"/></svg>
    <p>Data and<br>transaction security</p>
  </div>
</section>

<section class="about">
  <h2 class="h-section">About us</h2>
  <p class="abs copy">It is a long established fact that a reader will be distracted by the readable content of a page when looking at its layout. The point of using Lorem Ipsum is that it has a more-or-less normal distribution of letters, as opposed to using 'Content here, content here', making it look like readable English. Many desktop publishing packages and web page editors now use Lorem Ipsum as their default model text, and a search for 'lorem ipsum' will uncover many web sites still in their infancy. Various versions have evolved over the years, sometimes by accident, sometimes on purpose</p>
  <div class="abs btn-outline">Read More &raquo;</div>
  <div class="abs video-frame" role="img" aria-label="Video presentation still: oil barrel beside a rising arrow and green bar chart">
    <div class="abs play"><svg width="22" height="24" viewBox="0 0 22 24"><path d="M3 2l17 10L3 22z" fill="#1d2a3d"/></svg></div>
  </div>
</section>

<section class="purchaser">
  <h2 class="h-section">Oil purchaser</h2>
  <p class="abs lead">We provide the most powerful service</p>

  <div class="benefit" style="left:90px;top:190px">
    <div class="ring"><svg width="36" height="36" viewBox="0 0 36 36" fill="var(--orange)"><path d="M4 12l20-6 2 5-20 6z"/><path d="M14 14l-6 18h4l4-12 4 12h4l-6-18z"/><rect x="2" y="32" width="32" height="3"/></svg></div>
    <h3>Access to cheaper oil</h3>
    <p>It has survived not only five centuries, but also the leap into electronic</p>
  </div>
  <div class="benefit" style="left:90px;top:318px">
    <div class="ring"><svg width="36" height="36" viewBox="0 0 36 36" fill="var(--orange)"><rect x="7" y="4" width="18" height="28" rx="2"/><circle cx="26" cy="25" r="7" fill="#fff"/><path d="M26 19c-3 4-5 6-5 8a5 5 0 0 0 10 0c0-2-2-4-5-8z"/></svg></div>
    <h3>Convenience of online orders</h3>
    <p>It has survived not only five centuries, but also the leap into electronic</p>
  </div>
  <div class="benefit" style="left:761px;top:190px">
    <div class="ring"><svg width="36" height="36" viewBox="0 0 36 36" fill="var(--orange)"><rect x="6" y="4" width="10" height="28" rx="2"/><rect x="20" y="4" width="10" height="28" rx="2"/><rect x="8" y="9" width="6" height="3" fill="#fff"/><rect x="22" y="18" width="6" height="3" fill="#fff"/></svg></div>
    <h3>Transaction history</h3>
    <p>It has survived not only five centuries, but also the leap into electronic typesetting.</p>
  </div>
  <div class="benefit" style="left:761px;top:318px">
    <div class="ring"><svg width="36" height="36" viewBox="0 0 36 36" fill="var(--orange)"><rect x="6" y="6" width="16" height="26" rx="2"/><rect x="9" y="9" width="10" height="7" fill="#fff"/><path d="M22 12h5l3 4v12a2 2 0 0 1-4 0v-8h-4" fill="none" stroke="var(--orange)" stroke-width="2.5"/></svg></div>
    <h3>Order status monitoring</h3>
    <p>It has survived not only five centuries, but also the leap into electronic typesetting.</p>
  </div>

  <div class="abs rig" role="img" aria-label="Illustration of an offshore oil platform with a crane above the sea"></div>
</section>

<section class="seller">
  <h2 class="h-section">Oil seller</h2>
  <div class="perk" style="left:197px">
    <div class="ring"><svg width="36" height="36" viewBox="0 0 36 36"><path d="M4 4h14l14 14-14 14L4 18z" fill="#1c2a44"/><circle cx="11" cy="11" r="3" fill="#fff"/></svg></div>
    <h3>New sale channel</h3>
    <p>It has survived not only five centuries, but also the leap into electronic</p>
  </div>
  <div class="perk" style="left:464px">
    <div class="ring"><svg width="40" height="34" viewBox="0 0 40 34" fill="#1c2a44"><circle cx="20" cy="9" r="6"/><circle cx="8" cy="12" r="4.5"/><circle cx="32" cy="12" r="4.5"/><path d="M10 30c0-8 4-13 10-13s10 5 10 13z"/><path d="M0 28c0-6 3-10 8-10 2 0 3 1 4 2-2 2-3 5-3 8zM40 28c0-6-3-10-8-10-2 0-3 1-4 2 2 2 3 5 3 8z"/></svg></div>
    <h3>Attracting new clients</h3>
    <p>It has survived not only five centuries, but also the leap into electronic</p>
  </div>
  <div class="perk" style="left:734px">
    <div class="ring"><svg width="28" height="36" viewBox="0 0 28 36"><path d="M14 2C8 12 3 18 3 24a11 11 0 0 0 22 0c0-6-5-12-11-22z" fill="#1c2a44"/><path d="M9 24a5 5 0 0 0 5 5" stroke="#fff" stroke-width="2" fill="none"/></svg></div>
    <h3>More oil sold</h3>
    <p>It has survived not only five centuries, but also the leap into electronic</p>
  </div>
  <div class="perk" style="left:999px">
    <div class="ring"><svg width="32" height="36" viewBox="0 0 32 36"><path d="M16 2l13 5v10c0 9-6 15-13 17C9 32 3 26 3 17V7z" fill="#1c2a44"/><path d="M16 7v22c-5-2-8-6-8-12V10z" fill="#fff"/></svg></div>
    <h3>Transaction security</h3>
    <p>It has survived not only five centuries, but also the leap into electronic</p>
  </div>
</section>

<section class="contact">
  <h2 class="h-section" style="left:92px;top:98px">Crudeline</h2>
  <p class="abs copy">Lorem Ipsum has been the industry's standard dummy text ever since the 1500s, when an unknown printer took a galley of type and scrambled it to make a type specimen book. It has survived not only five centuries, but also the leap into electronic typesetting, remaining essentially unchanged. It was popularised in the 1960s with the release of Typeleaf sheets containing Lorem Ipsum passages, and more recently with desktop publishing software like Folio Layout including versions of Lorem Ipsum</p>
  <h2 class="h-section" style="left:638px;top:92px">Contact form</h2>
  <div class="field" style="left:642px;top:131px;width:228px">Name</div>
  <div class="field" style="left:884px;top:131px;width:228px">Email id</div>
  <div class="field" style="left:642px;top:192px;width:228px">Phone</div>
  <div class="field" style="left:884px;top:192px;width:228px">Subject</div>
  <div class="field" style="left:642px;top:250px;width:470px">Message</div>
  <div class="abs btn-submit">SUBMIT</div>
</section>

<footer class="site-footer">
  <div class="brand"><span class="brand-dot"></span>Crudeline</div>
  <h4 style="left:355px">Contact us</h4>
  <p class="abs footer-lines">Address : 12 Harbour Row, Eastgate<br>Fenwick, FN4 2QR<br>Phone : 555-014-2290.<br>Email : hello@crudeline.example</p>
  <h4 style="left:646px">Sign up for newsletter</h4>
  <p class="abs footer-note">Your about us information would fit here nicely.</p>
  <div class="abs news-input">Email address</div>
  <div class="abs news-btn">Submit</div>
  <h4 style="left:937px">Follow us out there</h4>
  <span class="social" style="left:937px"></span>
  <span class="social" style="left:975px"></span>
  <span class="social" style="left:1013px"></span>
  <span class="social" style="left:1051px"></span>
</footer>

<section class="copyright">Copyright &copy; 2017. All Rights Reserved</section>

</body>
</html>
```